Website and Logo Design for new niche job board.

Hello, We are an up and coming job board that is focused on LEGITIMATE companies that hire telecommuters to work from home. We are looking to build a highly interactive job board and forum/blog. The site is called WorkBreeze.com We focus on helping work at home moms, older workers and college students in work at home positions. We offer free job posting and advertising to the employer and free resume posting to the job seeker. (Free everything basically) Our revenue will be based from banner ads on the site so we will need a space on both sides of the page for those ads. 

The software we are using to build the job board part of the site can be viewed at www.sitevantor.example. It is already built! We do not need job software but a dashboard look to our main page - PLEASE pay attention to this! Do not submit a job board look as we have the job board page built!

These are the sites I like - please use these links to understand exactly the look I want

 

http://www.brightpebbles.example/

http://www.tessaverne.example/

http://www.ladiesatlabor.example/

https://www.findingnannies.example/index.asp?
Updates

Hi everyone- I think there might be some confusion to what we are looking for. We have the job board software through www.sitevantor.example, we are looking for the main page to be built around that. Basically we want a dashboard look with lots of little boxes to add content such as different articles,podcasts, forums,blogs,highlight different companies hiring,etc. If you can add scrolling or moving objects would be ideal. The less of a static website the better. You dont have to worry about the jobboard portion just the main page when you click on www.WorkBreeze.com, we really need it to capture peoples attention and see its a staffing firm AND a job board, forum, etc for work at home positions.  Here are some looks I am aiming for -

http://www.tessaverne.example/

Please use alot of color- lime green, oranges, turquiose blue, purple, lots and lots of color please! I like more tropical colors. Thanks! I dont like red and dark colors at all. Thanks

Target Market(s)

Target customers will be both companies and individuals. The individuals will be a broad age range that are interested in working from home. The companies will be small to large corporations that have valid work from home positions.

Requirements
Must have
• I want a colorful site with moving objects and scrolling text - static sites are bland, and outdated- I am looking for a HIGHLY interactive board. Please do not just throw a template up there and expect me to like it. I am picky and want an ultra sleek design and eye catching. I can make an out of the box website myself, I have 3 other companies and did that -  PLEASE PLEASE DO NOT SHOW ME A COOKIE!
Nice to have
• Would be very nice to have the HTML sliced up for finished designs.
Should not have
• just not boring and static. Anything new and creative is where we are heading.

```html
<!DOCTYPE html>
<html lang="en">
<head>
<meta charset="utf-8">
<title>WorkBreeze – Work From Home Jobs</title>
<link href="https://fonts.googleapis.com/css2?family=Dosis:wght@500;600;700&family=Noto+Sans:wght@400;700&display=swap" rel="stylesheet">
<style>
:root{
  --cyan:#2bb5dd;
  --cyan-dark:#1d9fc9;
  --pink:#df007c;
  --lime:#a8e43c;
  --lime-bright:#c6f51a;
  --grey:#6d6d6d;
  --ink:#111;
  --muted:#8a8a8a;
}
*{box-sizing:border-box;margin:0;padding:0}
html,body{width:722px;height:1200px;overflow:hidden;background:#fff}
body{font-family:"Noto Sans",Verdana,sans-serif;color:var(--ink)}
.page{position:absolute;left:0;top:0;width:1263px;height:2099px;transform:scale(0.5717);transform-origin:0 0;background:#fff}
.abs{position:absolute}
a{color:inherit;text-decoration:none}

.topbar{left:0;top:0;width:1263px;height:26px;background:var(--cyan);color:#fff;font-size:11px;font-weight:700;text-align:right;padding:8px 94px 0 0}
.topbar span{margin:0 6px}
.brand{left:90px;top:62px}
.brand-name{font-family:"Dosis",sans-serif;font-weight:700;font-size:46px;color:var(--pink);letter-spacing:1px}
.tagline{left:860px;top:68px;font-family:"Dosis",sans-serif;font-weight:700;font-size:19px;line-height:23px}
.nav{left:0;top:154px;width:1263px;height:38px;background:linear-gradient(#3ec3e8,var(--cyan-dark))}
.nav a{position:absolute;top:11px;color:#fff;font-family:"Dosis",sans-serif;font-weight:700;font-size:14px;letter-spacing:.3px}
.nav .home{left:168px;top:4px;width:90px;height:28px;background:var(--lime-bright);color:#222;text-align:center;padding-top:7px;border-radius:2px}
.navshade{left:0;top:192px;width:1263px;height:30px;background:linear-gradient(#e6e6e6,#fff)}

.section-title{font-family:"Dosis",sans-serif;font-weight:700;font-size:14px}

.blog-box{left:80px;top:278px;width:254px;height:128px;background:var(--pink);border-radius:10px;box-shadow:-6px 4px 0 #888;color:#fff;padding:12px 15px}
.blog-box h2{font-family:"Dosis",sans-serif;font-size:26px;font-weight:600}
.blog-box p{font-size:11px;font-weight:700;width:150px;line-height:13px;margin-top:4px}
.blog-box small{display:block;font-size:10px;font-weight:700;margin-top:6px}

.card{background:#fff;border:2px solid var(--cyan);border-radius:14px}
.feature{left:80px;top:445px;width:254px;height:528px;padding:20px 10px}
.feature h3{font-family:"Dosis",sans-serif;font-weight:600;font-size:19px;text-align:center;color:#444;line-height:22px}
.photo-tree{left:12px;top:70px;width:230px;height:214px;border:2px solid #555;background:linear-gradient(#eef3f6 0%,#7fae3a 30%,#4f8a24 60%,#9bbf6a 100%)}
.feature em{position:absolute;left:9px;top:296px;width:230px;font-size:14px;color:#666;line-height:17px}
.feature p{position:absolute;left:9px;top:368px;width:235px;font-size:11px;line-height:13px}
.read{font-size:10px;font-weight:700}

.forum{left:80px;top:1023px;width:252px;height:299px;border-radius:0 0 14px 14px;border-top:none}
.wave-head{left:-2px;top:0;width:252px;height:80px}
.forum-title,.types-title{left:10px;top:8px;color:#fff;font-family:"Dosis",sans-serif;font-weight:700;font-size:18px}
.list{font-size:11px;color:#444;list-style:none}
.list li{line-height:18px}
.list li::before{content:"-";margin-right:12px}

.types{left:80px;top:1376px;width:252px;height:234px;border-color:var(--pink);border-radius:0 0 14px 14px;border-top:none}

.find{left:80px;top:1675px;width:250px;height:250px;border-radius:50%;border:2px solid var(--cyan);overflow:hidden}
.find-top{left:0;top:0;width:250px;height:76px;background:var(--cyan);color:#fff;font-family:"Dosis",sans-serif;font-weight:700;font-size:18px;text-align:center;padding-top:28px}
.social{left:62px;width:126px;height:46px;font-family:"Dosis",sans-serif;font-weight:700;font-size:20px;text-align:center;padding-top:9px;border:2px solid #333;color:#333;background:#fff}
.social.one{top:94px}
.social.two{top:157px}

.jobs{left:351px;top:279px;width:484px;height:354px;border:2px solid #ccc;border-radius:12px;box-shadow:5px 4px 0 #aaa;background:#fff}
.tab{top:12px;height:20px;font-size:11px;font-weight:700;color:#fff;text-align:center;padding-top:3px;background:#111}
.tab.on{background:var(--cyan)}
.job-row{left:14px;width:456px;height:48px;background:#f3f3f3;border-bottom:1px solid #ddd;font-size:11px}
.job-row span{position:absolute}
.job-row .desc{left:86px;top:6px;line-height:13px;width:160px}
.job-row .desc b{display:block}

.post{left:359px;width:480px;height:80px}
.post .face{left:0;top:0;width:98px;height:78px}
.face.f{background:linear-gradient(135deg,#3a2418,#c58a66 45%,#e8c0a0)}
.face.m{background:linear-gradient(135deg,#2c2c2c,#a57058 45%,#d8b09a)}
.post h4{position:absolute;left:105px;top:10px;width:375px;font-size:12.5px;line-height:14px;letter-spacing:.3px}
.post small{position:absolute;left:105px;top:46px;font-size:12px;color:var(--muted)}

.employer{left:351px;top:1520px;width:483px;height:260px;border-radius:12px;box-shadow:5px 4px 0 #aaa;background:#fff;overflow:hidden}
.emp-badge{left:36px;top:78px;width:84px;height:84px;border:3px solid #ccc;border-radius:10px;background:#f2f2f2}
.emp-name{left:145px;top:76px;font-size:13px;font-weight:700}
.emp-text{left:145px;top:106px;width:275px;font-size:11px;line-height:13px}
.emp-more{left:329px;top:160px}
.emp-other{left:26px;top:176px;font-size:13px;font-weight:700}
.partner{top:205px;font-family:"Dosis",sans-serif;font-weight:700;font-size:34px;color:#555}

.tip{left:353px;top:1800px;width:808px;height:244px;border:2px solid var(--pink);border-radius:14px;overflow:hidden;background:#fff}
.tip-head{left:0;top:0;width:808px;height:58px;background:var(--pink);color:#fff;font-family:"Dosis",sans-serif;font-weight:700;font-size:24px;text-align:center;padding-top:14px}
.tip-body{left:0;top:58px;width:808px;height:186px;background:linear-gradient(#eee,#fff 40%)}
.tip .topics{left:18px;top:16px;font-size:12px;font-weight:700;color:#333}
.tip .tlist{left:18px;top:52px;font-size:11px;line-height:18px;color:#333;list-style:none}
.tip .lead{left:213px;top:16px;width:560px;font-size:11.5px;font-weight:700;line-height:14px}
.tip .para{left:213px;width:570px;font-size:11px;line-height:13px;color:#333}

.search{left:862px;top:278px;width:298px;height:260px;background:var(--lime);border-radius:12px;box-shadow:8px 0 0 #999;padding:20px 22px}
.search label{display:block;font-size:11px;font-weight:700;margin-bottom:5px}
.field{width:252px;height:27px;background:#fff;border:1px solid #888;font-size:11px;color:#888;padding:6px 6px;margin-bottom:15px}
.btn{background:var(--pink);color:#fff;font-size:11px;font-weight:700;text-align:center}
.search .btn{width:72px;height:23px;margin:2px auto;padding-top:4px}

.ad{background:#0b0b0b}
.poll{left:862px;top:812px;width:298px;height:232px;border:2px solid var(--pink);border-radius:12px;overflow:hidden;background:#f6f6f6}
.poll-head{left:0;top:0;width:298px;height:60px;background:var(--pink);color:#fff;font-family:"Dosis",sans-serif;font-weight:700;font-size:24px;text-align:center;padding-top:14px}
.poll .q{left:16px;top:66px;font-family:"Dosis",sans-serif;font-size:60px;color:#555}
.poll .ask{left:62px;top:86px;font-size:11px;color:#333}
.opt{left:76px;font-size:11px;color:#333;display:flex;align-items:center;gap:10px}
.opt i{display:block;width:17px;height:17px;border:1px solid #666;background:#fff}
.poll .btn{left:96px;top:197px;width:100px;height:23px;border-radius:12px;padding-top:4px}

.news{left:862px;top:1085px;width:299px;height:156px;background:var(--grey)}
.news-head{left:0;top:0;width:299px;height:38px;background:var(--pink);color:#fff;font-family:"Dosis",sans-serif;font-weight:700;font-size:18px;padding:7px 0 0 68px}
.news-icon{left:22px;top:-4px;width:40px;height:40px;border-radius:50%;background:#fff;border:2px solid #ddd}
.news label{position:absolute;left:8px;color:#fff;font-size:11px;font-weight:700}
.news .in{position:absolute;left:48px;width:241px;height:27px;background:#fff}
.news .btn{left:108px;top:131px;width:74px;height:18px;border-radius:9px;padding-top:2px}

.footer{left:0;top:2064px;width:1263px;height:35px;background:var(--cyan);color:#fff;font-size:11.5px;font-weight:700;text-align:center;padding-top:12px;letter-spacing:.5px}
</style>
</head>
<body>
<div class="page">

  <div class="abs topbar"><a>Login</a><span>|</span><a>Register</a><span>|</span><a>Contact Us</a></div>
  <div class="abs brand"><div class="brand-name">WORKBREEZE</div></div>
  <div class="abs tagline">When the pressure of traditional<br>employment gets to be too much...</div>

  <nav class="abs nav">
    <a class="home">HOME</a>
    <a style="left:323px">MY ACCOUNT</a>
    <a style="left:508px">FIND JOBS</a>
    <a style="left:667px">POST RESUME</a>
    <a style="left:845px">REGISTER</a>
    <a style="left:995px">EMPLOYER</a>
  </nav>
  <div class="abs navshade"></div>

  <section class="abs blog-box">
    <h2>Our blog</h2>
    <p>Lorem Ipsum is simply dummy text of the printing.</p>
    <small>Read More</small>
  </section>

  <section class="abs card feature">
    <h3>Lorem Ipsum is simply<br>dummy text</h3>
    <div class="abs photo-tree" role="img" aria-label="Photo of a large leafy tree in a meadow with two people sitting beneath it"></div>
    <em>Lorem Ipsum is simply dummy text of the printing and typesetting industry.</em>
    <p>Lorem Ipsum has been the industry's standard dummy text ever since the 1500s, when an unknown printer took a galley of type and scrambled it to make a type specimen book. It has survived not only five centuries, but also the leap into electronic typesetting, remaining essentially unchanged.</p>
    <span class="abs read" style="left:168px;top:488px">Read More</span>
  </section>

  <section class="abs card forum">
    <svg class="abs wave-head" viewBox="0 0 252 80" preserveAspectRatio="none"><path d="M0 0H252V80C200 50 120 40 0 45Z" fill="#2bb5dd"/></svg>
    <div class="abs forum-title">Work Breeze Forum</div>
    <p class="abs" style="left:9px;top:76px;width:232px;font-size:11px;line-height:16px;color:#444">List of Current topics being discussed in forum</p>
    <ul class="abs list" style="left:9px;top:126px">
      <li>Forum 1</li><li>Forum 2</li><li>Forum 3</li><li>Forum 4</li><li>Forum 5</li><li>Forum 6</li>
    </ul>
    <span class="abs read" style="left:165px;top:250px;font-size:11px;color:#333">Read More</span>
  </section>

  <section class="abs card types">
    <svg class="abs wave-head" viewBox="0 0 252 80" preserveAspectRatio="none"><path d="M0 0H252V80C200 50 120 40 0 45Z" fill="#df007c"/></svg>
    <div class="abs types-title">Types of Positions:</div>
    <ul class="abs list" style="left:20px;top:64px">
      <li>Accounts</li><li>Audits</li><li>Computer Software</li><li>Computer Data Entry</li><li>Graphic Designing</li><li>Logo Designing</li><li>S.E.O.</li><li>Web Designing</li>
    </ul>
  </section>

  <section class="abs find">
    <div class="abs find-top">Find us On:</div>
    <div class="abs social one">Circlebook</div>
    <div class="abs social two">Chirper</div>
  </section>

  <div class="abs section-title" style="left:367px;top:248px">LATEST JOBS</div>
  <section class="abs jobs">
    <div class="abs tab on" style="left:14px;width:114px">By Area of Interest</div>
    <div class="abs tab" style="left:137px;width:108px">By Field</div>
    <div class="abs tab" style="left:252px;width:108px">By Qualification</div>
    <div class="abs job-row" style="top:33px"><span style="left:8px;top:19px">April 05</span><span class="desc"><b>Data Entry</b>Lorem Ipsum is simply dummy text of the printing</span><span style="left:262px;top:19px">Tramo</span><b class="abs" style="left:304px;top:19px">Computer</b><span style="left:383px;top:19px">$10/Hour</span></div>
    <div class="abs job-row" style="top:81px"><span style="left:8px;top:19px">April 05</span><span class="desc"><b>Data Entry</b>Lorem Ipsum is simply dummy text of the printing</span><span style="left:262px;top:19px">Tramo</span><b class="abs" style="left:304px;top:19px">Computer</b><span style="left:383px;top:19px">$10/Hour</span></div>
    <div class="abs job-row" style="top:129px"><span style="left:8px;top:19px">April 05</span><span class="desc"><b>Data Entry</b>Lorem Ipsum is simply dummy text of the printing</span><span style="left:262px;top:19px">Tramo</span><b class="abs" style="left:304px;top:19px">Computer</b><span style="left:383px;top:19px">$10/Hour</span></div>
    <div class="abs job-row" style="top:180px"><span style="left:8px;top:19px">April 05</span><span class="desc"><b>Data Entry</b>Lorem Ipsum is simply dummy text of the printing</span><span style="left:262px;top:19px">Tramo</span><b class="abs" style="left:304px;top:19px">Computer</b><span style="left:383px;top:19px">$10/Hour</span></div>
    <div class="abs job-row" style="top:228px"><span style="left:8px;top:19px">April 05</span><span class="desc"><b>Data Entry</b>Lorem Ipsum is simply dummy text of the printing</span><span style="left:262px;top:19px">Tramo</span><b class="abs" style="left:304px;top:19px">Computer</b><span style="left:383px;top:19px">$10/Hour</span></div>
    <div class="abs job-row" style="top:276px"><span style="left:8px;top:19px">April 05</span><span class="desc"><b>Data Entry</b>Lorem Ipsum is simply dummy text of the printing</span><span style="left:262px;top:19px">Tramo</span><b class="abs" style="left:304px;top:19px">Computer</b><span style="left:383px;top:19px">$10/Hour</span></div>
  </section>

  <div class="abs section-title" style="left:367px;top:661px">BLOG POSTS</div>
  <article class="abs post" style="top:685px"><div class="abs face f" role="img" aria-label="Portrait photo of the post author"></div><h4>Lorem Ipsum is simply dummy text of the printing and typesetting industry.</h4><small>Posted by Pixelnest on 12/04/2010 at 12:00 AM</small></article>
  <article class="abs post" style="top:775px"><div class="abs face m" role="img" aria-label="Portrait photo of the post author"></div><h4>Lorem Ipsum is simply dummy text of the printing and typesetting industry.</h4><small>Posted by Pixelnest on 12/04/2010 at 12:00 AM</small></article>
  <article class="abs post" style="top:865px"><div class="abs face f" role="img" aria-label="Portrait photo of the post author"></div><h4>Lorem Ipsum is simply dummy text of the printing and typesetting industry.</h4><small>Posted by Pixelnest on 12/04/2010 at 12:00 AM</small></article>
  <article class="abs post" style="top:955px"><div class="abs face m" role="img" aria-label="Portrait photo of the post author"></div><h4>Lorem Ipsum is simply dummy text of the printing and typesetting industry.</h4><small>Posted by Pixelnest on 12/04/2010 at 12:00 AM</small></article>
  <article class="abs post" style="top:1045px"><div class="abs face f" role="img" aria-label="Portrait photo of the post author"></div><h4>Lorem Ipsum is simply dummy text of the printing and typesetting industry.</h4><small>Posted by Pixelnest on 12/04/2010 at 12:00 AM</small></article>
  <article class="abs post" style="top:1135px"><div class="abs face m" role="img" aria-label="Portrait photo of the post author"></div><h4>Lorem Ipsum is simply dummy text of the printing and typesetting industry.</h4><small>Posted by Pixelnest on 12/04/2010 at 12:00 AM</small></article>
  <article class="abs post" style="top:1225px"><div class="abs face f" role="img" aria-label="Portrait photo of the post author"></div><h4>Lorem Ipsum is simply dummy text of the printing and typesetting industry.</h4><small>Posted by Pixelnest on 12/04/2010 at 12:00 AM</small></article>
  <article class="abs post" style="top:1315px"><div class="abs face m" role="img" aria-label="Portrait photo of the post author"></div><h4>Lorem Ipsum is simply dummy text of the printing and typesetting industry.</h4><small>Posted by Pixelnest on 12/04/2010 at 12:00 AM</small></article>
  <article class="abs post" style="top:1405px"><div class="abs face f" role="img" aria-label="Portrait photo of the post author"></div><h4>Lorem Ipsum is simply dummy text of the printing and typesetting industry.</h4><small>Posted by Pixelnest on 12/04/2010 at 12:00 AM</small></article>

  <section class="abs employer">
    <svg class="abs" style="left:0;top:0" width="483" height="92" viewBox="0 0 483 92" preserveAspectRatio="none"><path d="M0 0H483V92C380 55 230 45 0 68Z" fill="#2bb5dd"/></svg>
    <div class="abs emp-badge"></div>
    <div class="abs emp-name">Harbor Mutual Insurance</div>
    <div class="abs emp-text">Lorem Ipsum is simply dummy text of the printing and typesetting industry. Lorem Ipsum has been the industry's standard dummy text ever since the 1500s.</div>
    <span class="abs read emp-more">Read More</span>
    <div class="abs emp-other">Other Employers</div>
    <div class="abs partner" style="left:30px">Vantello</div>
    <div class="abs partner" style="left:190px">Orvix</div>
    <div class="abs partner" style="left:355px">Brama</div>
  </section>

  <section class="abs tip">
    <div class="abs tip-head">TIP OF THE WEEK</div>
    <div class="abs tip-body">
      <div class="abs topics">Topics:</div>
      <ul class="abs tlist"><li>Lorum Ipsum</li><li>Lorum Ipsum</li><li>Lorum Ipsum</li><li>Lorum Ipsum</li><li>Lorum Ipsum</li><li>Lorum Ipsum</li></ul>
      <div class="abs lead">Contrary to popular belief, Lorem Ipsum is not simply random text. It has roots in a piece of classical Latin literature from 45 BC</div>
      <p class="abs para" style="top:60px">It is a long established fact that a reader will be distracted by the readable content of a page when looking at its layout. The point of using Lorem Ipsum is that it has a more-or-less normal distribution of letters, as opposed to using 'Content here, content here', making it look like readable English.</p>
      <p class="abs para" style="top:126px">Many desktop publishing packages and web page editors now use Lorem Ipsum as their default model text, and a search for 'lorem ipsum' will uncover many web sites still in their infancy.</p>
      <span class="abs read" style="left:701px;top:166px">Read More</span>
    </div>
  </section>

  <section class="abs search">
    <label>Job Title:</label><div class="field">(e.g., nurse)</div>
    <label>Skills/Keywords:</label><div class="field">(e.g., healthcare, sales)</div>
    <label>Location:</label><div class="field">(city, state, or zip code)</div>
    <div class="btn">Search</div>
  </section>

  <div class="abs ad" style="left:862px;top:570px;width:298px;height:207px;background:linear-gradient(135deg,#000 40%,#c8261a 55%,#000 70%)" role="img" aria-label="Banner advertisement with an illustrated bird of prey"></div>

  <section class="abs poll">
    <div class="abs poll-head">LIVE POLL:</div>
    <div class="abs q">?</div>
    <div class="abs ask">Is the Job Market getting better yet?</div>
    <div class="abs opt" style="top:114px"><i></i>Definitely!</div>
    <div class="abs opt" style="top:140px"><i></i>No Way</div>
    <div class="abs opt" style="top:167px"><i></i>What is a Job market?</div>
    <div class="abs btn">View Result</div>
  </section>

  <section class="abs news">
    <div class="abs news-head">Newsletter</div>
    <div class="abs news-icon"></div>
    <label style="top:56px">Name</label><div class="in" style="top:49px"></div>
    <label style="top:96px">Email</label><div class="in" style="top:89px"></div>
    <div class="abs btn">Subscribe</div>
  </section>

  <div class="abs ad" style="left:862px;top:1287px;width:298px;height:492px;background:linear-gradient(#0a0a14 0%,#1a1a2a 20%,#5a0e0e 25%,#0a0a0a 35%,#444 70%,#0a0a0a 90%)" role="img" aria-label="Advertisement for stainless steel enamel pet ID tags showing a round metal tag"></div>

  <footer class="abs footer">©2010 workbreeze.com - All Rights Reserved</footer>
</div>
</body>
</html>
```